Elmrow Management real estate management company needs presentation folder to hand clients

looking for a folder with pockets that represent my real estate management company when i hand to client reports or promotional material. I only do resedential real estate. I want classy and professional - pictures or additioal graphixs are fine

when a client open i will usally insert text and reports about my business
also on the inside flap is usally place for my business card i will upload a picture so the theme can be constant

Target Market(s)

my existing real estate cleints
and i will use when i am soliciting new business

Industry/Entity Type

Real Estate

Font styles to use
Serif

Requirements
Must have
• must have logo
• must give appearance of professionalism and maturity
• have basic company info tel# ,address
• id like viewer to know I manage real estate - focus on residential small to large apartment buildings
• not strip malls, not giganic complexes - im a mid size company
• logo is black but i welcome color as u see fit
Nice to have
• maybe pictures
• my slogan - " we will manage your building like its our own "
• focus on professioanl, safe, trust worthy
• type style should be clear and readable - but im open to sugestions

```html
<!DOCTYPE html>
<html lang="en">
<head>
<meta charset="utf-8">
<title>Elmrow Management Presentation Folder</title>
<link rel="stylesheet" href="https://fonts.googleapis.com/css2?family=Arimo:wght@400;700&family=Michroma&display=swap">
<style>
  :root {
    --page: #ffffff;
    --folder: #232323;
    --folder-deep: #0e0e0e;
    --paper: #ffffff;
    --ink: #111111;
    --brand: #4f9cb4;
    --rule: #8a8a8a;
  }
  * { margin: 0; padding: 0; box-sizing: border-box; }
  html, body { width: 1200px; height: 1200px; overflow: hidden; background: var(--page); }
  .canvas { position: relative; width: 1200px; height: 1200px; }

  .panel { position: absolute; top: 300px; width: 460px; height: 600px; background: var(--folder); overflow: hidden; }
  .panel--inside { left: 120px; }
  .panel--cover { left: 640px; }
  .panel svg.shapes { position: absolute; inset: 0; }

  .letterhead { position: absolute; left: 28px; top: 48px; width: 120px; font-family: "Arimo", sans-serif; color: var(--ink); }
  .letterhead .name { font-weight: 700; font-size: 12px; }
  .letterhead .title { font-size: 5px; letter-spacing: .2px; text-transform: uppercase; margin-bottom: 6px; }
  .letterhead .line { font-size: 5.5px; text-align: right; line-height: 1.35; }
  .letterhead .addr { font-size: 3.5px; margin-top: 3px; }

  .card { position: absolute; left: 278px; top: 46px; width: 160px; height: 92px; background: var(--paper); border: 3px solid #000; font-family: "Arimo", sans-serif; color: var(--ink); }
  .card .mark { position: absolute; left: 8px; top: 10px; width: 38px; height: 46px; border-right: 1px solid #000; }
  .card .mark span { display: block; width: 14px; height: 14px; background: #000; margin: 6px 0 3px 10px; }
  .card .mark em { font-style: normal; font-size: 4px; font-weight: 700; display: block; text-align: center; }
  .card .details { position: absolute; left: 52px; top: 10px; right: 6px; }
  .card .name { font-weight: 700; font-size: 10px; }
  .card .title { font-size: 4px; text-transform: uppercase; }
  .card .line { font-size: 4.5px; text-align: right; line-height: 1.3; }
  .card .addr { font-size: 3px; margin-top: 2px; white-space: nowrap; }
  .card .slogan { position: absolute; left: 6px; right: 6px; bottom: 6px; font-size: 3.6px; text-align: center; text-transform: uppercase; border-top: 2px solid #000; padding-top: 3px; }

  .brochure-label { position: absolute; left: 138px; top: 180px; width: 52px; display: flex; flex-direction: column; align-items: center; font-family: "Michroma", sans-serif; font-size: 40px; line-height: 47px; color: #fff; }

  .brand { position: absolute; display: flex; align-items: center; gap: 5px; font-family: "Arimo", sans-serif; font-weight: 700; color: var(--brand); white-space: nowrap; }
  .brand .dot { background: var(--brand); }
  .brand--small { right: 8px; bottom: 16px; font-size: 8px; }
  .brand--small .dot { width: 10px; height: 10px; }
  .brand--large { left: 50%; top: 420px; transform: translateX(-50%); font-size: 24px; }
  .brand--large .dot { width: 22px; height: 22px; }

  .cover-photo { position: absolute; left: 0; top: 150px; width: 290px; height: 230px; background: linear-gradient(160deg, #c9ccd2 0%, #6d7480 55%, #e0b79a 100%); }
</style>
</head>
<body>
<div class="canvas">

  <section class="panel panel--inside">
    <svg class="shapes" width="460" height="600" viewBox="0 0 460 600">
      <defs>
        <linearGradient id="sky" x1="0" y1="0" x2="0" y2="1">
          <stop offset="0" stop-color="#8fe2f8"/>
          <stop offset="1" stop-color="#4a9fb8"/>
        </linearGradient>
      </defs>
      <rect x="12" y="30" width="300" height="555" fill="#ffffff"/>
      <polygon points="300,30 460,30 460,600 0,600 0,585" fill="#232323"/>
      <polygon points="300,30 460,30 460,95 266,95" fill="#0e0e0e"/>
      <polygon points="130,166 369,166 220,559 130,559" fill="url(#sky)"/>
      <line x1="460" y1="400" x2="340" y2="600" stroke="#8a8a8a" stroke-width="1.2"/>
    </svg>

    <div class="letterhead">
      <div class="name">Daniel Marsh</div>
      <div class="title">Master Building Manager</div>
      <div class="line">office tel 914-555-0142</div>
      <div class="line">email dmarsh@elmrow.com</div>
      <div class="line">cell 917-555-0187</div>
      <div class="addr">48 Cedar Lane Floor 2 Harwick NY 10999</div>
    </div>

    <div class="card">
      <div class="mark"><span></span><em>ELMROW</em></div>
      <div class="details">
        <div class="name">Daniel Marsh</div>
        <div class="title">Master Building Manager</div>
        <div class="line">office tel 914-555-0142</div>
        <div class="line">email dmarsh@elmrow.com</div>
        <div class="line">cell 917-555-0187</div>
        <div class="addr">48 Cedar Lane Floor 2 Harwick NY 10999</div>
      </div>
      <div class="slogan">Your building kept in steady and caring hands</div>
    </div>

    <div class="brochure-label" aria-label="Brochure">
      <span>B</span><span>R</span><span>O</span><span>C</span><span>H</span><span>U</span><span>R</span><span>E</span>
    </div>

    <div class="brand brand--small"><span class="dot"></span>Elmrow Management</div>
  </section>

  <section class="panel panel--cover">
    <svg class="shapes" width="460" height="600" viewBox="0 0 460 600">
      <line x1="460" y1="400" x2="340" y2="600" stroke="#8a8a8a" stroke-width="1.2"/>
    </svg>
    <div class="cover-photo" role="img" aria-label="Photo of an open hand holding a small model house"></div>
    <div class="brand brand--large"><span class="dot"></span>Elmrow Management</div>
    <div class="brand brand--small"><span class="dot"></span>Elmrow Management</div>
  </section>

</div>
</body>
</html>
```